Eyebrow Tattooist business card design

I am an eyebrow specialist. I wax, shape, tint and tattoo eyebrows. I want a professional but classy image. I like gold raised writing on it. Colour of card either chocolate brown or pale blue??
As I use a technique called feathering and hair strokes, I would like the shape of a eyebrow on the front, with the hair strokes.

Industry/Entity Type
Tattoo
Contact Information for Business Card
I am an eyebrow specialist.
FRONT -  I want the name 'Glint Lashline' on the front of the card. With a shape of a brow, with every hair stroke. Need the words 'Tessa brow specialist and cosmetic tattooist' 'using feathered and hairstroke techniques'
03 5126-4730
BACK - At, Serene Glow Spa & Skin Studio. Shop 42, Hollin Park Market Arcade, Tamsworth-Delby Parade. Kelford Downs. Vic 3917.
www.glintlashline.com.au

```html
<!DOCTYPE html>
<html lang="en">
<head>
<meta charset="utf-8">
<title>Glint Lashline – Business Card</title>
<link rel="stylesheet" href="https://fonts.googleapis.com/css2?family=EB+Garamond:wght@400;700&display=swap">
<style>
  :root {
    --canvas: #e4e4e2;
    --brown: #6a4912;
    --gold: #d2a612;
    --paper: #f3f3f1;
    --serif: "EB Garamond", Georgia, serif;
  }
  * { box-sizing: border-box; margin: 0; padding: 0; }
  html, body {
    width: 1200px;
    height: 1000px;
    overflow: hidden;
    background: var(--canvas);
    font-family: var(--serif);
    color: var(--gold);
  }
  .canvas {
    position: relative;
    width: 1200px;
    height: 1000px;
  }
  .card {
    position: absolute;
    left: 250px;
    width: 700px;
    height: 428px;
    box-shadow: 0 6px 18px rgba(0,0,0,0.18);
  }
  .card--front { top: 42px; background: var(--brown); }
  .card--back { top: 530px; display: flex; }

  /* Front */
  .front-brand {
    position: absolute;
    left: 0; right: 0;
    top: 150px;
    text-align: center;
  }
  .brand-name {
    display: inline-flex;
    align-items: center;
    gap: 16px;
    font-weight: 700;
    font-size: 74px;
    line-height: 1;
    letter-spacing: 0.5px;
  }
  .brand-dot {
    width: 18px; height: 18px;
    border-radius: 50%;
    background: var(--gold);
  }
  .front-tagline {
    margin-top: 14px;
    font-weight: 700;
    font-size: 21px;
  }
  .front-rule {
    width: 420px;
    height: 1.5px;
    background: var(--gold);
    margin: 8px auto 8px;
  }
  .front-technique {
    font-size: 18px;
    letter-spacing: 0.6px;
  }

  /* Back */
  .back-identity {
    width: 46%;
    background: var(--paper);
    padding: 150px 28px 0 34px;
    position: relative;
  }
  .back-identity .brand-name { font-size: 44px; gap: 10px; }
  .back-identity .brand-dot { width: 11px; height: 11px; }
  .back-identity .brand-tagline {
    font-weight: 700;
    font-size: 12.5px;
    margin-top: 6px;
  }
  .person {
    margin-top: 40px;
    text-align: right;
    padding-right: 14px;
  }
  .person-name { font-weight: 700; font-size: 20px; }
  .person-role {
    font-size: 16px;
    text-align: left;
    margin-top: 2px;
  }
  .back-contact {
    flex: 1;
    background: var(--brown);
    padding: 110px 30px 0 36px;
    font-size: 19px;
    line-height: 1.3;
  }
  .address { font-style: normal; }
  .phone { margin-top: 14px; }
  .web { margin-top: 22px; }
</style>
</head>
<body>
<main class="canvas">

  <section class="card card--front" aria-label="Card front">
    <div class="front-brand">
      <div class="brand-name"><span class="brand-dot"></span>Glint Lashline</div>
      <p class="front-tagline">Tessa brow specialist and cosmetic tattooist</p>
      <div class="front-rule"></div>
      <p class="front-technique">using feathered and hairstroke techniques</p>
    </div>
  </section>

  <section class="card card--back" aria-label="Card back">
    <div class="back-identity">
      <div class="brand-name"><span class="brand-dot"></span>Glint Lashline</div>
      <p class="brand-tagline">Tessa brow specialist and cosmetic tattooist</p>
      <div class="person">
        <p class="person-name">Tessa</p>
        <p class="person-role">Brow Specialist and cosmetic tattooist</p>
      </div>
    </div>
    <div class="back-contact">
      <address class="address">
        Serene Glow Spa &amp; Skin Studio<br>
        Shop 42, Hollin Park Market Arcade<br>
        Tamsworth-Delby Parade<br>
        Kelford Downs<br>
        Vic 3917.
      </address>
      <p class="phone">03 5126-4730</p>
      <p class="web">www.glintlashline.com.au</p>
    </div>
  </section>

</main>
</body>
</html>
```